Harborstone Lending Business Card Design

We are looking for a nice looking business card design. I'd prefer something other than white for the background but white is ok if necessary. I'm uploading two versions of my picture, one is square and one is rounded. Also a couple of versions of the logo for white backgrounds as well as one for darker backgrounds.

Target Market(s)

Realtors and prospective clients

Industry/Entity Type

Mortgage

Contact Information for Business Card

Double sided business card. Not sure what is needed here.

Colors

Designer to choose colors to be used in the design.

Requirements
Must have
• Name: Marcus Pellham
• Title: Senior Mortgage Advisor
• Email: marcuspellham@harborstonelending.example
• website: www.marcuspellhamhomeloangroup.example
• Address: 4670 W 2850 N, STE 215 Salt Lake City, UT 84192
• Phone: 801-555-0187
• nmls# 948217
• Logo is on our webstie. www.harborstonelending.example
• Picture
Nice to have
• Colors could be similar to our website www.harborstonelending.example
• A list of what we do (VA Loans, FHA Loans, Conventional Loans, USDA Loans)

```html
<!DOCTYPE html>
<html lang="en">
<head>
<meta charset="utf-8">
<title>Harborstone Lending – Business Card</title>
<link href="https://fonts.googleapis.com/css2?family=Alegreya:wght@400;500;700&family=Arimo:wght@400&display=swap" rel="stylesheet">
<style>
  :root {
    --bg: #7b8280;
    --charcoal: #333433;
    --green: #6e9e2e;
    --paper: #f6f6f6;
    --ink: #2a2a2a;
    --light: #ececec;
  }
  * { margin: 0; padding: 0; box-sizing: border-box; }
  html, body { width: 1200px; height: 803px; overflow: hidden; }
  body {
    background: var(--bg);
    font-family: "Alegreya", Georgia, serif;
    position: relative;
  }
  .card {
    position: absolute;
    top: 150px;
    width: 294px;
    height: 503px;
    overflow: hidden;
  }
  .card-back { left: 283px; background: var(--charcoal); }
  .card-front { left: 623px; background: var(--paper); }

  .stripes { position: absolute; left: 0; width: 100%; }
  .stripes span {
    display: block; height: 7px; background: var(--green); margin-bottom: 4px;
  }

  /* back */
  .brand {
    position: absolute; top: 235px; width: 100%;
    text-align: center; color: var(--light);
  }
  .brand-dot {
    width: 34px; height: 34px; border-radius: 50%;
    background: var(--light); margin: 0 auto 14px;
  }
  .brand-name {
    font-family: "Alegreya", Georgia, serif;
    font-weight: 700; font-size: 25px; letter-spacing: 1px;
    text-transform: uppercase;
  }
  .card-back .stripes { top: 370px; }

  /* front */
  .portrait {
    position: absolute; left: 87px; top: 21px;
    width: 120px; height: 132px; border-radius: 50%;
    border: 4px solid var(--green);
    background: radial-gradient(ellipse at 50% 45%, #b98a6e 0%, #8a5a3c 45%, #6b4a2a 75%, #3d3a36 100%);
  }
  .name {
    position: absolute; top: 160px; width: 100%; text-align: center;
    color: var(--green); font-size: 20px; font-weight: 500;
  }
  .title {
    position: absolute; top: 184px; width: 100%; text-align: center;
    font-family: "Arimo", Arial, sans-serif; font-size: 12px; color: var(--ink);
  }
  .contact {
    position: absolute; top: 220px; width: 100%;
    list-style: none; text-align: center; color: var(--ink);
    font-size: 11px; line-height: 1.2;
  }
  .contact li { height: 28.5px; }
  .contact svg { display: block; margin: 0 auto 1px; width: 12px; height: 12px; fill: var(--green); }
  .card-front .stripes { top: 372px; }
  .services-panel {
    position: absolute; top: 402px; left: 0; width: 100%; bottom: 0;
    background: var(--charcoal);
  }
  .services {
    list-style: none; position: absolute; left: 92px; top: 20px;
    color: var(--light); font-size: 12px; line-height: 16px;
  }
  .services li { display: flex; align-items: center; gap: 9px; }
  .services svg { width: 11px; height: 11px; fill: var(--green); }
</style>
</head>
<body>

<section class="card card-back">
  <div class="brand">
    <div class="brand-dot"></div>
    <div class="brand-name">Harborstone Lending</div>
  </div>
  <div class="stripes"><span></span><span></span><span></span></div>
</section>

<section class="card card-front">
  <div class="portrait" role="img" aria-label="Portrait photo of Marcus Pellham"></div>
  <h1 class="name">Marcus Pellham</h1>
  <p class="title">Senior Mortgage Advisor</p>

  <ul class="contact">
    <li>
      <svg viewBox="0 0 24 24"><path d="M6.6 10.8a15 15 0 0 0 6.6 6.6l2.2-2.2c.3-.3.7-.4 1-.2 1.1.4 2.3.6 3.6.6.6 0 1 .4 1 1V20c0 .6-.4 1-1 1A17 17 0 0 1 3 4c0-.6.4-1 1-1h3.5c.6 0 1 .4 1 1 0 1.3.2 2.5.6 3.6.1.3 0 .7-.2 1z"/></svg>
      801-555-0187
    </li>
    <li>
      <svg viewBox="0 0 24 24"><path d="M2 5h20v14H2z M3 6l9 7 9-7" stroke="#f6f6f6" stroke-width="1.5"/></svg>
      marcuspellham@harborstonelending.example
    </li>
    <li>
      <svg viewBox="0 0 24 24"><circle cx="12" cy="12" r="10"/></svg>
      www.marcuspellhamhomeloangroup.example
    </li>
    <li>
      <svg viewBox="0 0 24 24"><path d="M12 2a7 7 0 0 0-7 7c0 5 7 13 7 13s7-8 7-13a7 7 0 0 0-7-7zm0 9.5A2.5 2.5 0 1 1 12 6.5a2.5 2.5 0 0 1 0 5z"/></svg>
      4670 W 2850 N, Suite 215, Salt Lake City, Utah 84192
    </li>
    <li>
      <svg viewBox="0 0 24 24"><path d="M9 2h2l-1 6h4l1-6h2l-1 6h4v2h-4l-1 4h4v2h-4l-1 6h-2l1-6h-4l-1 6H7l1-6H4v-2h4l1-4H5V8h4zm1 8-1 4h4l1-4z"/></svg>
      NMLS# 948217
    </li>
  </ul>

  <div class="stripes"><span></span><span></span><span></span></div>

  <div class="services-panel">
    <ul class="services">
      <li><svg viewBox="0 0 24 24"><path d="M12 2l3 7h7l-5.5 4.5 2 7.5-6.5-4.5-6.5 4.5 2-7.5L2 9h7z"/></svg>VA Loans</li>
      <li><svg viewBox="0 0 24 24"><path d="M12 2l3 7h7l-5.5 4.5 2 7.5-6.5-4.5-6.5 4.5 2-7.5L2 9h7z"/></svg>FHA Loans</li>
      <li><svg viewBox="0 0 24 24"><path d="M12 2l3 7h7l-5.5 4.5 2 7.5-6.5-4.5-6.5 4.5 2-7.5L2 9h7z"/></svg>Conventional Loans</li>
      <li><svg viewBox="0 0 24 24"><path d="M12 2l3 7h7l-5.5 4.5 2 7.5-6.5-4.5-6.5 4.5 2-7.5L2 9h7z"/></svg>USDA Loans</li>
    </ul>
  </div>
</section>

</body>
</html>
```